The Lantern Pact a non-fiction book on mindfulness COVER design needed

A non-fiction book about active mindfulness.
The Lantern Pact includes 21 different daily 'dares' which are action based activities to generate positive mindfulness - to become more contented with life.
Based on the teeaching of the New Thought movements of the early 20th century, think The Hollow, Climb and Gather Plenty.
The book is positive and uplifting. It fits into the self-help / spiritual / health segments. It skews female 40 to 50 year olds.
Think fresh colours like a bold orange or bright green.
What needs to be on the cover:
TITLE: The Lantern Pact
AUTHOR: Marcus Tindall
BLURB: Get clarity, focus, and a new zest for life by following The Lantern Pact for just 21 days.
Target Market(s)
Women 40-50 english speaking
Industry/Entity Type
Self-help / Health

```html
<!DOCTYPE html>
<html lang="en">
<head>
<meta charset="utf-8">
<title>The Lantern Pact — Book Cover</title>
<link rel="stylesheet" href="https://fonts.googleapis.com/css2?family=Bebas+Neue&display=swap">
<style>
  :root {
    --backdrop: #efebe6;
    --cover-green: #8cc63f;
    --ink-black: #231f20;
    --paper-white: #ffffff;
  }
  * { margin: 0; padding: 0; box-sizing: border-box; }
  html, body {
    width: 1200px;
    height: 1000px;
    overflow: hidden;
    background: var(--backdrop);
  }
  .canvas {
    position: relative;
    width: 1200px;
    height: 1000px;
  }
  .book-cover {
    position: absolute;
    left: 255px;
    top: 34px;
    width: 690px;
    height: 932px;
    background: var(--cover-green);
    overflow: hidden;
    font-family: "Bebas Neue", "Arial Narrow", sans-serif;
  }
  .rule {
    position: absolute;
  }
  .rule--top {
    left: 520px;
    top: 0;
    width: 20px;
    height: 250px;
    background: var(--paper-white);
  }
  .rule--bottom {
    left: 330px;
    top: 690px;
    width: 20px;
    height: 242px;
    background: var(--ink-black);
  }
  .author {
    position: absolute;
    left: 74px;
    top: 62px;
    font-size: 58px;
    line-height: 1;
    letter-spacing: 0.16em;
    color: var(--ink-black);
  }
  .title {
    position: absolute;
    left: 0;
    top: 0;
    width: 100%;
    font-weight: 400;
  }
  .title__word {
    position: absolute;
    display: block;
    font-size: 196px;
    line-height: 0.8;
  }
  .title__word--the {
    right: 70px;
    top: 232px;
    color: var(--paper-white);
  }
  .title__word--lantern {
    right: 70px;
    top: 392px;
    color: var(--ink-black);
  }
  .title__word--pact {
    left: 322px;
    top: 548px;
    color: var(--ink-black);
  }
  .blurb {
    position: absolute;
    left: 382px;
    top: 712px;
    font-size: 29px;
    line-height: 31.5px;
    letter-spacing: 0.02em;
    color: var(--paper-white);
  }
  .blurb span { display: block; }
</style>
</head>
<body>
  <main class="canvas">
    <article class="book-cover">
      <div class="rule rule--top"></div>
      <div class="rule rule--bottom"></div>

      <p class="author">Marcus Tindall</p>

      <h1 class="title">
        <span class="title__word title__word--the">THE</span>
        <span class="title__word title__word--lantern">LANTERN</span>
        <span class="title__word title__word--pact">PACT</span>
      </h1>

      <p class="blurb">
        <span>GET CLARITY,</span>
        <span>FOCUS, AND</span>
        <span>A NEW ZEST</span>
        <span>FOR LIFE</span>
        <span>BY FOLLOWING</span>
        <span>THE LANTERN PACT</span>
        <span>FOR JUST 21 DAYS</span>
      </p>
    </article>
  </main>
</body>
</html>
```